Orthopedist website

We need a web design for a relaunch of this website: http://www.gelenkwerk-praxis.example/
This website is for a orthopedist. Please fell free to create a modern and clean layout. The currently used colours need not to be used in the new design.
The website should transport reliability so that patients will call or contact the doctor for a treatment.
A specially logo is not available.
Reason: We will get a new logo which should be integrated into the design.
Reason: Customer will get a new logo (is ready soon).
Target Market(s)
The target market are patients from salzburg / austria which have orthopedic problems (hand, feet, backbone)
Industry/Entity Type
Doctor
Look and feel

```html
<!DOCTYPE html>
<html lang="de">
<head>
<meta charset="utf-8">
<title>Orthopädie Dr. Berger</title>
<link href="https://fonts.googleapis.com/css2?family=Open+Sans:ital,wght@0,400;0,600;0,700;1,400&family=Questrial&display=swap" rel="stylesheet">
<style>
:root{
  --navy:#1d3a7a;
  --blue:#2a8ac8;
  --blue-head:#2d7fc1;
  --text:#7a7a7a;
  --dark:#222;
  --line:#d9d9d9;
  --panel:#f2f2f2;
  --white:#fff;
}
*{box-sizing:border-box;margin:0;padding:0}
html,body{width:1200px;height:1076px;overflow:hidden;background:var(--white)}
body{position:relative;font-family:Arial,Helvetica,sans-serif;color:var(--text)}
.abs{position:absolute}
.brand{left:150px;top:14px;display:flex;align-items:center;gap:10px}
.brand-mark{width:22px;height:22px;background:var(--navy)}
.brand-name{font-family:"Open Sans",sans-serif;font-weight:600;font-size:15px;color:var(--navy)}
.contact-head{right:150px;top:16px;text-align:right;font-size:13px;line-height:16px;color:var(--text)}
.contact-head .doctor{font-weight:700;font-size:13.5px;color:var(--blue-head)}
.contact-head .phone{font-weight:700;font-size:21px;line-height:24px;color:var(--blue-head)}
.nav{left:150px;top:121px;width:900px;height:41px;display:flex;border:1px solid #e3e3e3;border-bottom:3px solid var(--navy);border-left:none}
.nav a{display:flex;align-items:center;padding:0 19.5px;font-size:13.5px;color:#333;text-decoration:none;border-right:1px solid #e3e3e3}
.nav a.active{background:var(--navy);color:var(--white)}
.nav a:last-child{border-right:none;flex:1;justify-content:center}
.hero{left:152px;top:182px;width:897px;height:398px;background:linear-gradient(180deg,#8fb6dc 0%,#b9d2e8 42%,#9fb3b8 52%,#c9a77a 68%,#b8915e 100%)}
.hero h1{position:absolute;left:28px;top:140px;width:440px;font-family:"Open Sans",sans-serif;font-weight:700;font-size:29px;line-height:34px;color:var(--white);text-shadow:0 1px 3px rgba(0,0,0,.3)}
.hero p{position:absolute;left:30px;top:226px;width:406px;font-size:13px;line-height:17px;color:var(--white);text-align:justify}
.dots{position:absolute;left:33px;top:359px;display:flex;gap:9px}
.dots span{width:10px;height:10px;border-radius:50%;background:var(--white)}
.dots span.on{background:var(--blue)}
.welcome{left:151px;top:613px;width:600px}
.welcome h2{font-family:"Questrial",sans-serif;font-weight:400;font-size:23.5px;color:var(--navy);letter-spacing:.2px}
.welcome .sub{font-style:italic;font-size:13.5px;color:var(--dark);margin-top:-1px}
.welcome .body{margin-top:18px;width:600px;font-size:13.5px;line-height:17px;text-align:justify}
.welcome .body p+p{margin-top:17px}
.info{top:850px;width:281px;height:136px;color:var(--white);padding:12px 16px}
.info h3{font-size:17.5px;font-weight:400;letter-spacing:.3px;margin-bottom:8px}
.hours{left:150px;background:var(--blue)}
.hours .row{display:flex;justify-content:space-between;font-size:13.5px;padding:7px 2px 6px;border-bottom:1px solid rgba(255,255,255,.25)}
.hours .row:last-child{border-bottom:none}
.contact{left:469px;background:var(--navy)}
.contact .row{display:flex;align-items:center;gap:8px;font-size:13.5px;padding:6px 0 7px}
.contact svg{width:12px;height:14px;fill:var(--white);flex:none}
.booking{left:797px;top:615px;width:253px;height:370px;background:var(--panel)}
.booking h3{height:46px;background:var(--blue);color:var(--white);text-align:center;font-family:"Open Sans",sans-serif;font-weight:700;font-size:19px;line-height:46px}
.booking .field{margin:26px 14px 0;height:33px;background:var(--white);border:1px solid #e6e6e6;font-size:13.5px;color:#b5b5b5;padding:0 12px;line-height:31px}
.booking .field+.field{margin-top:17px}
.booking .submit{position:absolute;right:15px;bottom:30px;background:var(--blue);color:var(--white);font-weight:700;font-size:13.5px;padding:8px 14px;letter-spacing:.3px}
.footer-line{left:150px;top:1026px;width:900px;border-top:1px dotted #bbb}
.footer{top:1043px;font-family:"Open Sans",sans-serif;font-size:12.5px;color:#888}
.footer .name{color:var(--navy)}
.footer-left{left:151px}
.footer-right{right:150px}
</style>
</head>
<body>
<div class="abs brand"><span class="brand-mark"></span><span class="brand-name">Gelenkwerk Praxis</span></div>

<div class="abs contact-head">
  <div class="doctor">DR.MED. LUKAS M BERGER</div>
  <div class="phone">+43 662 000 12 34</div>
  <div>Gelenkwerk-Praxis Nord</div>
  <div>Lindenhofstr. 24</div>
  <div>5020 Salzburg</div>
</div>

<nav class="abs nav">
  <a class="active">Startseite</a>
  <a>Über die Praxis</a>
  <a>Leistungsspektrum</a>
  <a>Patienteninfo</a>
  <a>Aktuelles</a>
  <a>Kontakt</a>
  <a>Ihr Weg zu uns</a>
  <a>Impressum</a>
</nav>

<section class="abs hero" role="img" aria-label="Photo of two people jogging along a sandy beach by the sea under a blue sky">
  <h1>HERZLICH WILLKOMMEN BEI ORTHOPÄDIE DR.BERGER</h1>
  <p>Lorem ipsum dolor sit amet, consectetur adipiscing elit. Nam quis porttitor libero, ac accumsan felis. Vivamus faucibus sapien ac dapibus rhoncus.</p>
  <div class="dots"><span></span><span class="on"></span><span></span></div>
</section>

<section class="abs welcome">
  <h2>HERZLICH WILLKOMMEN BEI ORTHOPÄDIE DR.BERGER</h2>
  <div class="sub">Lorem ipsum dolor sit amet</div>
  <div class="body">
    <p>Mit dieser Internetseite stellen wir Ihnen eine Informationsplattform rund um unsere Arztpraxis bereit. Im Rahmen unserer fachärztlich orthopädischen Tätigkeit bieten wir ein breites Spektrum sowohl "schulmedizinischer" als auch "komplementärmedizinischer" Methoden von der Untersuchung über manuelle Therapieformen, diversen Injektionstechniken bis hin zu den aktuellen, auch minimalinvasiven Techniken der modernen orthopädischen Chirurgie an.</p>
    <p>Lernen Sie hier unsere Leistungen und unser Praxis-Team kennen.</p>
  </div>
</section>

<section class="abs info hours">
  <h3>OPENING HOURS</h3>
  <div class="row"><span>Monday - Friday</span><span>8.00 - 17.00</span></div>
  <div class="row"><span>Saturday</span><span>9.30 - 17.30</span></div>
  <div class="row"><span>Sunday</span><span style="margin-right:34px">Closed</span></div>
</section>

<section class="abs info contact">
  <h3>CONTACT US</h3>
  <div class="row"><svg viewBox="0 0 12 14"><path d="M6 0a4.5 4.5 0 0 0-4.5 4.5C1.5 8 6 14 6 14s4.5-6 4.5-9.5A4.5 4.5 0 0 0 6 0zm0 6.3a1.8 1.8 0 1 1 0-3.6 1.8 1.8 0 0 1 0 3.6z"/></svg>Lindenhofstr. 24 5020 Salzburg</div>
  <div class="row"><svg viewBox="0 0 12 14"><path d="M3 1l2 3-1.3 1.3c.5 1.6 1.5 3 3 4L8 8l3 2-1.5 2.5C5 12 1.5 7 1 2.5z"/></svg>+43 662 000 12 34</div>
  <div class="row"><svg viewBox="0 0 12 14"><path d="M3 1l2 3-1.3 1.3c.5 1.6 1.5 3 3 4L8 8l3 2-1.5 2.5C5 12 1.5 7 1 2.5z"/></svg>info@gelenkwerk-praxis.example</div>
</section>

<aside class="abs booking">
  <h3>MAKE A BOOKING</h3>
  <div class="field">Your First Name (required)</div>
  <div class="field">Your Last Name</div>
  <div class="field">Your Phone (required)</div>
  <div class="field">Your Email</div>
  <div class="field">Date of Appointment</div>
  <div class="submit">SUBMIT</div>
</aside>

<div class="abs footer-line"></div>
<div class="abs footer footer-left">Copyright © 2014 <span class="name">ORTHOPÄDIE DR.BERGER.</span> All right reserved.</div>
<div class="abs footer footer-right">Terms &amp; Condition &nbsp;|&nbsp; Privacy Policy</div>
</body>
</html>
```